Home Page PSD Website Design - 1 Page *

Design an eye-catching home page design for a rubbish removal website.

Please review the document provided it contains all the details and there is a second document with all the content for the page that needs to be included.

Target Market(s)

Home owners, businesses, property managers, real estate agents

Industry/Entity Type

Waste Management

Number of Pages Required

1 page

Requirements
Must have
• Please review the document provided it contains all the details and there is a second document with all the content for the page that needs to be included.

PSD must be layered, all elements labeled and separated for easy coding.
Nice to have

```html
<!DOCTYPE html>
<html lang="en">
<head>
<meta charset="utf-8">
<title>Brisk Junk Haulers – Home Page</title>
<link href="https://fonts.googleapis.com/css2?family=Montserrat:wght@300;400;700&family=Arimo:wght@400;700&display=swap" rel="stylesheet">
<style>
:root{
  --olive:#7b8c12;
  --lime:#a9bf1c;
  --dark-olive:#4b5600;
  --blue:#1565b0;
  --grey:#e8e8e8;
  --grey-soft:#efefef;
  --ink:#1a1a1a;
  --body:#333;
  --white:#fff;
  --black:#000;
}
*{margin:0;padding:0;box-sizing:border-box}
html,body{width:960px;height:1200px;overflow:hidden;background:var(--black)}
.stage{position:absolute;left:0;top:0;width:1725px;height:2156px;transform:scale(.5565);transform-origin:0 0;background:var(--black);font-family:"Arimo",Arial,sans-serif;color:var(--ink)}
.page{position:absolute;background:var(--white);width:564px;overflow:hidden}
.page--main{left:214px;top:13px;height:2118px}
.page--detail{left:966px;top:13px;height:1897px}
.abs{position:absolute}
.heading{font-family:"Montserrat",sans-serif;font-weight:400;color:var(--olive);text-align:center;text-transform:uppercase;left:0;width:100%;font-size:20px;letter-spacing:.2px}
.heading b{font-weight:700}
.heading--dark{color:var(--ink)}
p{line-height:1.25}

/* header */
.brand{left:62px;top:20px;display:flex;align-items:center;gap:4px;font-weight:700;font-size:9.5px;line-height:1;color:var(--blue);width:80px}
.brand .mark{flex:none;width:9px;height:9px;background:var(--lime)}
.nav{left:152px;top:29px;display:flex;gap:9px;font-size:7.5px;color:var(--ink);white-space:nowrap}
/* hero */
.hero{left:0;top:48px;width:564px;height:240px;background:linear-gradient(135deg,#c9bd2c,#e3d96a 45%,#b8ab1c)}
.hero-card{left:72px;top:66px;width:192px}
.hero-card .title{background:var(--blue);color:var(--white);padding:16px 12px 12px;font-weight:700;font-size:18px;line-height:1.2}
.hero-card .title small{display:block;font-size:14px;letter-spacing:.5px}
.hero-card .text{background:var(--white);padding:10px 12px 20px;font-size:7.8px;color:var(--ink);height:135px}
.hero-card .text p+p{margin-top:9px}
.mascot{left:345px;top:55px;width:120px;height:275px;background:linear-gradient(180deg,#8a6a45,#2f6fb8 40%,#2a55a0 70%,#b5b5b5);border-radius:40px 40px 8px 8px}
/* services */
.intro{left:78px;top:366px;width:414px;font-size:9.6px;line-height:1.32}
.svc-img{top:453px;height:87px;width:130px}
.svc-title{top:552px;font-size:12.5px;color:var(--olive);line-height:1;text-transform:uppercase}
.svc-text{top:590px;width:130px;font-size:8.4px;line-height:1.38}
.more{color:var(--blue);font-size:7px;text-transform:uppercase}
/* quote band */
.quote-band{left:0;top:733px;width:564px;height:204px;background:var(--grey)}
.quote-band .band-title{top:40px;font-size:15.5px}
.quote-band .text{left:95px;top:70px;width:376px;font-size:8.6px;line-height:1.45}
.btn{background:var(--blue);color:var(--white);font-weight:700;text-align:center;text-transform:uppercase}
.quote-band .btn{left:212px;top:140px;width:153px;height:28px;line-height:28px;font-size:12px}
/* gallery */
.shot{width:146px;height:192px}
.tag{position:absolute;left:0;bottom:0;background:var(--lime);color:var(--white);font-size:9px;padding:2px 5px}
/* why */
.why{left:0;top:1370px;width:564px;height:748px;background:var(--lime)}
.why .why-title{top:28px;font-size:19px}
.card{background:var(--white);width:132px;padding:12px 12px;font-size:6.2px;line-height:1.5;color:var(--body)}
.card h3{font-weight:400;font-size:12px;line-height:1.2;color:var(--ink);margin-bottom:8px}
.why .specialty{top:570px;font-size:19px;text-transform:none}
.specialty-text{left:60px;top:606px;width:444px;font-size:8.8px;line-height:1.45}
.specialty-text p+p{margin-top:9px}
/* detail column */
.list-box{left:62px;width:440px;background:var(--grey);display:flex;justify-content:space-around;padding-top:18px;font-size:6.8px;line-height:1.55;text-align:center}
.remark{left:208px;top:449px;width:285px;font-size:11.6px;line-height:1.35}
.mascot-small{left:102px;top:402px;width:82px;height:130px;background:linear-gradient(180deg,#8a6a45,#2f6fb8 50%,#b5b5b5);border-radius:30px 30px 6px 6px}
.steps{left:0;top:572px;width:564px;height:188px;background:var(--grey-soft)}
.steps .lead{left:0;top:0;width:212px;height:188px;background:var(--lime);padding:24px 0 0 62px;font-size:16.5px;line-height:1.5;color:var(--ink)}
.step{left:227px;width:300px;font-size:7.8px;line-height:1.45}
.step b{display:block;color:var(--olive);font-size:10.5px}
.arrow{width:28px;height:28px;top:888px}
.avatar{left:247px;top:862px;width:70px;height:70px;border-radius:50%;background:#a3a3a3}
.testimonial{left:85px;top:949px;width:395px;text-align:center;font-size:7px;color:#555;line-height:1.3}
.form-wrap{left:0;top:1034px;width:564px;height:410px;background:var(--grey-soft)}
.form-wrap .green{left:283px;top:0;width:281px;height:410px;background:var(--lime)}
.form-title{left:63px;top:32px;font-size:16.5px;font-weight:400;line-height:1.1;color:var(--olive)}
.form-text{left:63px;top:84px;width:190px;font-size:8px;line-height:1.5;color:var(--body)}
.field{left:298px;width:203px;height:14px;background:var(--white);font-size:8px;padding:1px 3px;color:var(--ink)}
.form-label{left:300px;font-size:7.8px;color:var(--ink)}
.check{display:inline-block;width:7px;height:7px;background:var(--white);margin-right:5px;vertical-align:middle}
.form-wrap .btn{height:19px;line-height:19px;font-size:8.5px}
.areas{top:1534px;width:110px;text-align:center;font-size:12px;line-height:1.3}
.eco{left:0;top:1661px;width:564px;height:169px;background:var(--blue)}
.eco .badge{left:88px;top:30px;width:94px;height:94px;border-radius:50%;background:#3aa03a;border:4px solid #cfe9cf}
.eco .text{left:216px;top:25px;width:270px;color:var(--white);font-size:8.3px;line-height:1.5}
.eco .text p+p{margin-top:10px}
.footer{left:55px;top:1848px;font-size:6.2px;line-height:1.9;color:var(--ink)}
.social{top:1857px;width:18px;height:20px;background:var(--blue)}
</style>
</head>
<body>
<div class="stage">

  <section class="page page--main">
    <div class="abs brand"><span class="mark"></span><span>Brisk Junk<br>Haulers</span></div>
    <nav class="abs nav"><span>HOME</span><span>AVAILABLE SERVICES</span><span>EASY ONLINE QUOTES</span><span>SERVICE AREAS</span><span>FAQ</span><span>CONTACT</span></nav>

    <div class="abs hero" role="img" aria-label="Photo of a cluttered room filled with old furniture and junk, tinted yellow"></div>
    <div class="abs hero-card">
      <div class="title">Got Junk to Haul?<small>GIVE US A CALL.</small></div>
      <div class="text">
        <p>Has your Barrie home, garage, basement, yard or place of business become cluttered with old appliances, furniture, electronics, yard debris, garbage or unwanted items that you have no use for?</p>
        <p>Call Brisk Junk Haulers today and let us help make extra space in your home and around your property by removing all that stuff you no longer have use for.</p>
      </div>
    </div>
    <div class="abs mascot" role="img" aria-label="Cartoon hero mascot lifting an armchair, TV and toys above a fridge and yard waste bucket"></div>

    <h2 class="abs heading" style="top:328px">Who do we service?</h2>
    <p class="abs intro">Whether you’re a Barrie homeowner, real estate agent, business owner, contractor, landlord, property manager or handling an estate, we’ve got you covered with our hassle-free &amp; speedy junk removal services. Sit back and relax while our crew does all the heavy lifting, carrying, loading and removal for you so you don’t have to. Just show us what needs to be removed and our team will take care of rest.</p>

    <div class="abs svc-img" style="left:79px;background:linear-gradient(180deg,#cfd8e0,#8a8580 55%,#5a6a3a)" role="img" aria-label="Photo of a large suburban house"></div>
    <div class="abs svc-img" style="left:218px;background:linear-gradient(180deg,#5d8fc8,#8fa9c0 55%,#6a9a40)" role="img" aria-label="Photo of a modern glass office building"></div>
    <div class="abs svc-img" style="left:357px;background:linear-gradient(180deg,#b5c7d8,#7d7f82 60%,#5e6468)" role="img" aria-label="Photo of an apartment tower"></div>

    <div class="abs svc-title" style="left:79px">Residential<br>Services</div>
    <div class="abs svc-title" style="left:218px">Commercial<br>Services</div>
    <div class="abs svc-title" style="left:355px">Property Managers<br>and Realtors</div>

    <p class="abs svc-text" style="left:79px">We know how quickly unwanted items, junk &amp; debris can pile up inside and outside of your home. With our fast, reliable junk removal service we can get your space back to normal the same-day. Did you know? Most items we remove are re-homed, donated or recycled! <span class="more">Show more</span></p>
    <p class="abs svc-text" style="left:218px">Our commercial junk removal service includes the cleanup of offices, retail spaces, warehouses, storage units and any other commercial space that needs to be cleared of junk, trash and unwanted items. <span class="more">Show more</span></p>
    <p class="abs svc-text" style="left:357px;top:592px">We help property managers clear out clutter as well as take old furniture, appliances, trash and mattresses that tenants left behind or have dumped illegally on the property. This helps you get your units rented faster and keep your properties looking clean. <span class="more">Show more</span></p>

    <div class="abs quote-band">
      <h2 class="abs heading heading--dark band-title">Get your easy online quote <b>today!</b></h2>
      <p class="abs text">We make it really easy for you to receive your junk removal quote. With the power of the internet there is no need to disrupt your busy schedule with an in-person quote. To get started simply click the link below and you will be taken to our online quote form. You will receive your junk removal quote quickly and hassle free.</p>
      <div class="abs btn">Click Here</div>
    </div>

    <div class="abs shot" style="left:56px;top:960px;background:linear-gradient(160deg,#6b5a48,#a88e6c 50%,#8a8a8a)" role="img" aria-label="Before photo of a garage packed with junk"><span class="tag">BEFORE</span></div>
    <div class="abs shot" style="left:209px;top:960px;background:linear-gradient(160deg,#3a3028,#b89a70 55%,#7a7a7a)" role="img" aria-label="Before photo of a storage unit full of pallets and boxes"><span class="tag">BEFORE</span></div>
    <div class="abs shot" style="left:363px;top:960px;background:linear-gradient(160deg,#5a4838,#8c7a62 50%,#4e4e4e)" role="img" aria-label="Before photo of a garage piled with bags and boxes"><span class="tag">BEFORE</span></div>
    <div class="abs shot" style="left:56px;top:1153px;background:linear-gradient(180deg,#7a6048,#a69a88 50%,#b5b5b0)" role="img" aria-label="After photo of the empty garage"><span class="tag">AFTER</span></div>
    <div class="abs shot" style="left:209px;top:1153px;background:linear-gradient(180deg,#4a4a4a,#b0ada5 50%,#c0bdb5)" role="img" aria-label="After photo of the empty storage unit"><span class="tag">AFTER</span></div>
    <div class="abs shot" style="left:363px;top:1153px;background:linear-gradient(180deg,#8a6a48,#a68a68 50%,#b8b5ae)" role="img" aria-label="After photo of the cleared garage"><span class="tag">AFTER</span></div>

    <div class="abs why">
      <h2 class="abs heading heading--dark why-title">Why <b>choose</b> us?</h2>

      <div class="abs card" style="left:65px;top:76px;height:171px"><h3>On Time, Every Time!</h3>You want to get your home or business back to normal as quickly as possible and without delay. That is why when you choose Brisk Junk Haulers you can rest assured your junk will be removed on time, every time! You will never have to worry about no-shows, excuses or delays that are so common with “fly by night” junk removal services.</div>
      <div class="abs card" style="left:215px;top:76px;height:171px"><h3>Fully Insured</h3>When hiring a local junk removal service, it’s important to check that the company you are hiring has liability insurance. If someone is injured around your home and they are not carrying their own insurance, you can be held legally liable for their medical bills, lost wages, physical therapy and even the cost of a lawsuit if they decide to sue. This is why you should always make sure the junk removal service you are considering hiring is fully insured.</div>
      <div class="abs card" style="left:366px;top:76px;height:171px"><h3>Protecting the Environment</h3>Our Green initiative goes beyond industry standards. If we can salvage, re-use, recycle, donate, or refurbish your unwanted items, WE WILL! We provide you peace of mind knowing that when you hire us for junk removal, your waste material is recycled to help protect our environment.</div>

      <div class="abs card" style="left:65px;top:262px;height:130px"><h3>No Hidden Fees</h3>We are upfront about our pricing, with no hidden service charges or environmental fees. Your investment is clearly laid out for you before we commence.</div>
      <div class="abs card" style="left:215px;top:262px;height:130px"><h3>Big or Small We Take it All!</h3>Whether you just have a single couch to remove or a complete garage full of stuff, we can help. We take on jobs both big and small.</div>
      <div class="abs card" style="left:366px;top:262px;height:130px"><h3>Locally Owned</h3>Family run and locally owned means you will always receive personal, courteous and friendly service. Service with a smile all while saving you money! When you call us you will be speaking to the owners of the business allowing us to better serve you!</div>

      <div class="abs card" style="left:65px;top:407px;height:112px"><h3>Speedy Service</h3>Our name says it all. Same day or next day junk removal available 7 days a week from 7am – 9pm. After hour appointments are also available.</div>
      <div class="abs card" style="left:215px;top:407px;height:112px"><h3>Cleaning Up</h3>At the end of each job, we provide complete job site cleanup. Your living space will be just as clean as or cleaner than it was when we first arrived.</div>
      <div class="abs card" style="left:366px;top:407px;height:112px"><h3>Easy Online Quotes</h3>We make it really easy for you to receive your Junk Removal Quote. With the power of the internet there is no need to disrupt your busy schedule with an in-person estimate. Click Here to get your easy online quote today!</div>

      <h2 class="abs heading heading--dark specialty">Junk Removal is <b>Our Specialty</b>.</h2>
      <div class="abs specialty-text">
        <p>Over time, every business and household is sure to accumulate a number of unwanted items that end up collecting dust and taking up space. By contacting a junk hauling specialist to help you get rid of those items, you are saving yourself hours of hard work and possibly several trips to the dump. Brisk Junk Haulers can do all that for you promptly and efficiently, making sure that you don’t have to lift a finger or waste any precious time.</p>
        <p>Take advantage of our professional junk removal service to clean out your Barrie home, basement, garage or any other storage area of all types of unwanted items you want gone with ease. We can also clear away any rubbish and debris from your backyard and around your property.</p>
      </div>
    </div>
  </section>

  <section class="page page--detail">
    <h2 class="abs heading" style="top:32px">What we <b>can</b> remove for you</h2>
    <div class="abs list-box" style="top:70px;height:166px">
      <div>Carpets<br>Washers &amp; Dryers<br>Sofas / Couches<br>Play Equipment<br>Recyclable Items<br>Furniture<br>Refrigerators<br>Rubbish<br>Renovation Debris<br>Hot Tubs<br>Yard Waste<br>Mattresses</div>
      <div>Microwaves<br>Bed Frames<br>Old Clothing<br>Unwanted Toys<br>Tables<br>Chairs<br>Patio Furniture<br>Office Furniture<br>Appliances<br>TV’s &amp; Electronics<br>Entertainment Centers<br>Computers &amp; Printers</div>
      <div>Cabinets<br>Sinks, Tubs &amp; Household Fixtures<br>Pool Tables<br>Ping Pong Tables<br>Hutches<br>Dressers<br>Desks<br>Pianos<br>Exercise Equipment<br>Household Garbage<br>Tires<br>And Much More!</div>
    </div>

    <h2 class="abs heading" style="top:262px">What <b>can’t</b> we remove?</h2>
    <div class="abs list-box" style="top:297px;height:92px;padding-top:20px">
      <div>Hazardous Waste<br>Herbicides &amp; Pesticides<br>Chemical Waste<br>Oil/Antifreeze/Fuel<br>Wet Paint</div>
      <div>Animal Carcasses<br>Explosive Items<br>Bleach/Cleaners<br>Mold/Asbestos<br>Pressurized containers</div>
      <div style="margin-top:-4px">Concrete &amp; Bricks<br>Gravel &amp; Dirt<br>Roofing Shingles</div>
    </div>

    <div class="abs mascot-small" role="img" aria-label="Small cartoon hero mascot carrying household junk"></div>
    <p class="abs remark">We specialize in cleaning out individual rooms, whole houses, apartment buildings, storage units, office buildings, warehouses, schools, estates and even retail spaces across Barrie and surrounding areas.</p>

    <div class="abs steps">
      <div class="abs lead">Getting Rid of<br>Unwanted Items,<br>Junk &amp; Debris is<br>As <b>Easy as<br>1, 2, 3 !</b></div>
      <p class="abs step" style="top:24px"><b>Step 1:</b>Use our easy online quote form to get your quote today!</p>
      <p class="abs step" style="top:60px"><b>Step 2:</b>Schedule a day that works best for you. Same day, next day and after hour appointments are available.</p>
      <p class="abs step" style="top:110px"><b>Step 3:</b>When our friendly, uniformed team arrives they make everything super simple for you! All you have to do is point to your unwanted items and we’ll make them disappear</p>
    </div>

    <h2 class="abs heading" style="top:822px">What our clients say</h2>
    <svg class="abs arrow" style="left:60px" viewBox="0 0 28 28"><circle cx="14" cy="14" r="14" fill="#4b5600"/><path d="M18 8 L8 14 L18 20 Z" fill="#fff"/></svg>
    <svg class="abs arrow" style="left:474px" viewBox="0 0 28 28"><circle cx="14" cy="14" r="14" fill="#4b5600"/><path d="M10 8 L20 14 L10 20 Z" fill="#fff"/></svg>
    <div class="abs avatar" role="img" aria-label="Placeholder client avatar"></div>
    <p class="abs testimonial">“Lorem ipsum dolor sit amet, consectetur adipiscing elit, sed do eiusmod tempor incididunt ut labore et dolore magna aliqua. Ut enim ad minim veniam, quis nostrud exercitation ullamco laboris nisi ut aliquip ex ea commodo consequat..”<br>- John Doe</p>

    <div class="abs form-wrap">
      <div class="abs green"></div>
      <h2 class="abs form-title">Get Your Easy Online<br>Quote Today!</h2>
      <p class="abs form-text">We make it really easy for you to receive your junk removal quote. With the power of the internet there is no need to disrupt your busy schedule with an in-person quote. To get started simply click the link below and you will be taken to our online quote form. You will receive your junk removal quote quickly and hassle free.</p>
      <div class="abs field" style="top:33px">Name</div>
      <div class="abs field" style="top:52px">Email</div>
      <div class="abs field" style="top:70px">Phone</div>
      <div class="abs field" style="top:89px">City</div>
      <div class="abs field" style="top:108px">Address</div>
      <div class="abs field" style="top:127px">Residence type<svg style="position:absolute;right:3px;top:3px" width="9" height="7" viewBox="0 0 9 7"><path d="M0 0 H9 L4.5 7 Z" fill="#222"/></svg></div>
      <div class="abs field" style="top:146px;height:50px">Description of Items</div>
      <div class="abs form-label" style="top:202px">Where Are Items Located?</div>
      <div class="abs form-label" style="top:218px"><span class="check"></span>Upstairs</div>
      <div class="abs form-label" style="top:234px"><span class="check"></span>Basement</div>
      <div class="abs form-label" style="top:250px"><span class="check"></span>Main Floor</div>
      <div class="abs form-label" style="top:266px"><span class="check"></span>Garage</div>
      <div class="abs form-label" style="left:395px;top:217px"><span class="check"></span>Outside Yard</div>
      <div class="abs form-label" style="left:395px;top:233px"><span class="check"></span>Curbside Ready</div>
      <div class="abs form-label" style="left:395px;top:249px"><span class="check"></span>Other, Please</div>
      <div class="abs form-label" style="left:407px;top:265px">Describe ________</div>
      <div class="abs form-label" style="top:281px">If items are located in a building is there access</div>
      <div class="abs form-label" style="top:297px">to an elevator? <span class="check" style="margin-left:6px"></span>Yes <span class="check" style="margin-left:6px"></span>No</div>
      <div class="abs field" style="top:311px;height:51px">Questions or Comments</div>
      <div class="abs btn" style="left:298px;top:373px;width:109px">Upload Pictures</div>
      <div class="abs btn" style="left:425px;top:373px;width:71px">Submit</div>
    </div>

    <h2 class="abs heading" style="top:1493px;font-size:19px">Areas we <b>service</b> (about 260,000)</h2>
    <div class="abs areas" style="left:145px">Barrie<br>Innisfil<br>Angus<br>Springwater<br>Midhurst</div>
    <div class="abs areas" style="left:324px">Minesing<br>Shanty Bay<br>Oro Medonte<br>Essa (21,000)<br>Elmvale</div>

    <div class="abs eco">
      <div class="abs badge" role="img" aria-label="Round green eco badge"></div>
      <div class="abs text">
        <p>As your experienced waste removal experts, we know firsthand how vital proper trash disposal is. Not only is it the law, but it also helps keep junk from filling up our landfills.</p>
        <p>We donate or recycle as much clutter as we can, giving them a second home. We separate any green debris or yard waste as well, avoiding municipal waste bins. As long as any personal belongings can still help someone else, they get donated locally.</p>
      </div>
    </div>

    <div class="abs footer">Copyright 2021. Brisk Junk Haulers<br>All Rights Reserved.<br>Home &nbsp;|&nbsp; Available Services &nbsp;|&nbsp; Easy Online Quotes &nbsp;|&nbsp; Service Areas &nbsp;|&nbsp; FAQ &nbsp;|&nbsp; Contact</div>
    <div class="abs social" style="left:468px" role="img" aria-label="Social profile link"></div>
    <div class="abs social" style="left:493px" role="img" aria-label="Social profile link"></div>
  </section>

</div>
</body>
</html>
```